Business Card Design for Brightkeel

The company provides engineering tender consulting services and personnel resources. The target market is large engineering construction and services companies. The business is based in Australia.

```html
<!DOCTYPE html>
<html lang="en">
<head>
<meta charset="utf-8">
<title>Brightkeel Business Card</title>
<link rel="stylesheet" href="https://fonts.googleapis.com/css2?family=Barlow:wght@400;500&family=Barlow+Semi+Condensed:wght@500&display=swap">
<style>
  :root {
    --ink: #060606;
    --signal-red: #e40d0d;
    --paper: #ffffff;
    --soft-white: #f4f4f4;
    --shadow: rgba(0, 0, 0, 0.28);
  }
  * { margin: 0; padding: 0; box-sizing: border-box; }
  html, body {
    width: 1096px;
    height: 1200px;
    overflow: hidden;
    background: var(--paper);
    font-family: "Barlow", Arial, sans-serif;
  }
  .stage { position: relative; width: 1096px; height: 1200px; }

  .card {
    position: absolute;
    left: 179px;
    width: 720px;
    height: 436px;
    overflow: hidden;
    box-shadow: 6px 14px 22px var(--shadow);
  }
  .card--front { top: 94px; background: var(--ink); }
  .card--back { top: 608px; background: var(--signal-red); }

  .card__glow { position: absolute; inset: 0; }

  .brand-square {
    position: absolute;
    width: 98px;
    height: 98px;
  }
  .card--front .brand-square { left: 35px; top: 29px; background: var(--signal-red); }
  .card--back .brand-square { left: 594px; top: 29px; background: var(--ink); }

  .wordmark {
    position: absolute;
    font-family: "Barlow Semi Condensed", Arial, sans-serif;
    font-weight: 500;
    color: var(--soft-white);
    line-height: 1;
    white-space: nowrap;
  }
  .card--front .wordmark {
    right: 59px;
    top: 26px;
    font-size: 64px;
    letter-spacing: -0.5px;
  }

  .holder {
    position: absolute;
    left: 358px;
    top: 336px;
    color: var(--soft-white);
    white-space: nowrap;
  }
  .holder__name { font-size: 24px; font-weight: 500; letter-spacing: 0.5px; }
  .holder__title { font-size: 18px; margin-left: 8px; }

  .contact-band {
    position: absolute;
    left: 0;
    top: 370px;
    width: 100%;
    height: 66px;
    background: var(--signal-red);
    color: var(--soft-white);
    font-size: 17.5px;
    line-height: 24px;
  }
  .contact-band__col { position: absolute; top: 8px; white-space: nowrap; }
  .contact-band__col--address { left: 29px; }
  .contact-band__col--online { left: 358px; }
  .contact-band__col--phone { left: 570px; }

  .capabilities {
    position: absolute;
    top: 153px;
    left: 114px;
    display: grid;
    grid-template-columns: 211px auto;
    grid-auto-flow: column;
    grid-template-rows: repeat(5, 31px);
    color: var(--soft-white);
    font-size: 24px;
    line-height: 31px;
    list-style: none;
  }

  .capability-band {
    position: absolute;
    left: 0;
    top: 373px;
    width: 587px;
    height: 63px;
    background: var(--ink);
    color: var(--soft-white);
    font-size: 24px;
    line-height: 63px;
    padding-left: 37px;
  }
  .card--back .wordmark {
    left: 587px;
    top: 373px;
    width: 133px;
    height: 63px;
    line-height: 63px;
    text-align: center;
    font-size: 25px;
    color: var(--soft-white);
  }
</style>
</head>
<body>
<main class="stage">

  <section class="card card--front" aria-label="Business card front">
    <svg class="card__glow" width="720" height="436" viewBox="0 0 720 436" aria-hidden="true">
      <defs>
        <radialGradient id="front-sheen" cx="0.55" cy="0.3" r="0.5">
          <stop offset="0" stop-color="#3a3a3a" stop-opacity="0.55"/>
          <stop offset="1" stop-color="#060606" stop-opacity="0"/>
        </radialGradient>
      </defs>
      <rect width="720" height="436" fill="url(#front-sheen)"/>
    </svg>
    <div class="brand-square"></div>
    <div class="wordmark">Brightkeel</div>

    <p class="holder">
      <span class="holder__name">MARLOWE</span><span class="holder__title">President Director</span>
    </p>

    <div class="contact-band">
      <p class="contact-band__col contact-band__col--address">PO Box 99 Nnnnnnnnnn, NNN, 9999<br>ABN99999999999</p>
      <p class="contact-band__col contact-band__col--online">E: nnnn@nnn.com.au<br>W: www.brightkeel.au</p>
      <p class="contact-band__col contact-band__col--phone">M: 9999 999 999<br>T: 99 9999 9999</p>
    </div>
  </section>

  <section class="card card--back" aria-label="Business card back">
    <svg class="card__glow" width="720" height="436" viewBox="0 0 720 436" aria-hidden="true">
      <defs>
        <radialGradient id="back-sheen" cx="0.4" cy="0.15" r="0.55">
          <stop offset="0" stop-color="#f0502a" stop-opacity="0.6"/>
          <stop offset="1" stop-color="#e40d0d" stop-opacity="0"/>
        </radialGradient>
      </defs>
      <rect width="720" height="436" fill="url(#back-sheen)"/>
    </svg>
    <div class="brand-square"></div>

    <ul class="capabilities">
      <li>Our Capability</li>
      <li>Our Capability</li>
      <li>Our Capability</li>
      <li>Our Capability</li>
      <li>Our Capability</li>
      <li>Our Capability</li>
      <li>Our Capability</li>
      <li>Our Capability</li>
      <li>Our Capability</li>
      <li>Our Capability</li>
    </ul>

    <div class="capability-band">Our Capability</div>
    <div class="wordmark">Brightkeel</div>
  </section>

</main>
</body>
</html>
```